Business Card for Fashion House

We need a business card design for our personalize fashion service for our customers. the business card should reflect reliability, luxury and creativity.
The brand Vastrelle is extracted from "Vibrant Estrella"; Vastrelle provides fashion designs sprinkled with luxury and style tailored for our elite clients character profile.
Vastrelle is created for those who embody class and elegance with a passion for style.
Target Market(s)
Affluent Customers
Industry/Entity Type
Fashion
Contact Information for Business Card
Noura Al Hashimi
Fashion Designer
Telephone: +971 5550192
Mobile +971 555073
Emal q@k.example
Website www.vastrelle.example
Social Media Youtube g+ Facebook Instagram Pin /vastrelle
Font styles to use
Other font styles liked:
- Audrey provided
Look and feel
Each slider illustrates characteristics of the customer's brand and the style your logo design should communicate.

```html
<!DOCTYPE html>
<html lang="en">
<head>
<meta charset="utf-8">
<title>Vastrelle — Business Card</title>
<link rel="stylesheet" href="https://fonts.googleapis.com/css2?family=Marcellus&family=Open+Sans:wght@400;700&display=swap">
<style>
  :root {
    --stage: #1e1f21;
    --card-dark: #2f2f30;
    --card-dark-ink: #474748;
    --card-light: #f4f4f4;
    --ink: #2b2b2b;
    --ink-soft: #3a3a3a;
    --rule: #333333;
  }
  * { box-sizing: border-box; margin: 0; padding: 0; }
  html, body { width: 1200px; height: 900px; overflow: hidden; }
  body {
    background: var(--stage);
    font-family: "Open Sans", sans-serif;
    display: flex;
    flex-direction: column;
    align-items: center;
    justify-content: center;
    gap: 24px;
  }
  .card {
    position: relative;
    width: 640px;
    height: 366px;
  }
  .card--back {
    background: var(--card-dark);
    display: flex;
    align-items: center;
    justify-content: center;
  }
  .back-wordmark {
    font-family: "Marcellus", serif;
    font-size: 30px;
    letter-spacing: 12px;
    color: var(--card-dark-ink);
    text-transform: uppercase;
    padding-left: 12px;
  }
  .card--front {
    background: linear-gradient(135deg, #ececec 0%, var(--card-light) 45%, #fafafa 100%);
    color: var(--ink);
  }
  .brand {
    position: absolute;
    left: 60px;
    top: 74px;
    display: flex;
    align-items: center;
    gap: 14px;
  }
  .brand-dot {
    width: 12px;
    height: 12px;
    border-radius: 50%;
    background: var(--ink);
  }
  .brand-name {
    font-family: "Marcellus", serif;
    font-size: 26px;
    letter-spacing: 11px;
    text-transform: uppercase;
    color: var(--ink);
  }
  .divider {
    position: absolute;
    left: 58px;
    right: 42px;
    top: 236px;
    height: 0;
    border-top: 1.5px solid var(--rule);
  }
  .person {
    position: absolute;
    right: 44px;
    top: 188px;
    text-align: right;
  }
  .person-name { font-weight: 700; font-size: 18px; color: var(--ink); }
  .person-title { font-size: 15px; color: var(--ink-soft); margin-top: 1px; }
  .address {
    position: absolute;
    left: 58px;
    top: 252px;
    font-size: 14px;
    line-height: 20px;
    color: var(--ink-soft);
  }
  .contacts {
    position: absolute;
    left: 300px;
    top: 258px;
    list-style: none;
    font-size: 15px;
    line-height: 22px;
    color: var(--ink-soft);
  }
  .contacts li { display: flex; align-items: center; gap: 10px; }
  .contacts svg { width: 12px; height: 12px; flex: none; }
</style>
</head>
<body>
  <section class="card card--back" aria-label="Card back">
    <span class="back-wordmark">Vastrelle</span>
  </section>

  <section class="card card--front" aria-label="Card front">
    <div class="brand">
      <span class="brand-dot"></span>
      <span class="brand-name">Vastrelle</span>
    </div>

    <div class="person">
      <p class="person-name">Noura Al Hashimi</p>
      <p class="person-title">Fashion Designer</p>
    </div>

    <div class="divider"></div>

    <address class="address" style="font-style:normal">
      14 Palm Lane, Marina Road<br>
      Harbour side, CA 402117.
    </address>

    <ul class="contacts">
      <li>
        <svg viewBox="0 0 24 24" aria-hidden="true"><path fill="#3a3a3a" d="M6.6 10.8a15.1 15.1 0 0 0 6.6 6.6l2.2-2.2c.3-.3.7-.4 1-.2 1.1.4 2.3.6 3.6.6.6 0 1 .4 1 1V20c0 .6-.4 1-1 1A17 17 0 0 1 3 4c0-.6.4-1 1-1h3.5c.6 0 1 .4 1 1 0 1.3.2 2.5.6 3.6.1.3 0 .7-.2 1z"/></svg>
        +971 5550192
      </li>
      <li>
        <svg viewBox="0 0 24 24" aria-hidden="true"><path fill="#3a3a3a" d="M2 5h20v14H2z"/><path fill="none" stroke="#f4f4f4" stroke-width="2" d="M3 6l9 7 9-7"/></svg>
        q@k.example
      </li>
      <li>
        <svg viewBox="0 0 24 24" aria-hidden="true"><circle cx="12" cy="12" r="10" fill="#3a3a3a"/><path fill="none" stroke="#f4f4f4" stroke-width="1.4" d="M2 12h20M12 2c3 3 3 17 0 20M12 2c-3 3-3 17 0 20"/></svg>
        www.vastrelle.example
      </li>
    </ul>
  </section>
</body>
</html>
```